Create a business promotion flyer to leave in customer mailboxes. We are a bulk petroleum supplier, servicing any industry that requires diesel. Base in griffith NSW, servicing griffith area and surrounds.

Business Name - Terra Diesel
Fuel@terradiesel-example.com.au
Marco - 0412 309 768 mpellucci@terradiesel-example.com.au
Liam - 0431 672 095 lhartwell@terradiesel-example.com.au
Simon - 0465 218 347 sbrack@terradiesel-example.com.au
Office 02 6931 7852

Bulk Fuel deliveries.
Oils & lubricants
Local Family owned business

```html
<!DOCTYPE html>
<html lang="en">
<head>
<meta charset="utf-8">
<title>Terra Diesel – Bulk Fuel Supplier Flyer</title>
<link rel="stylesheet" href="https://fonts.googleapis.com/css2?family=Poppins:wght@400;500;600;700&family=Roboto+Condensed:wght@400;600;700&display=swap">
<style>
  :root{
    --red:#e3262b;
    --dark:#26272b;
    --ink:#1f2024;
    --white:#ffffff;
    --stage:#606060;
    --light-grey:#ececec;
    --sky-top:#2f6fc6;
    --sky-low:#a9c4e4;
    --concrete:#cfccc7;
  }
  *{box-sizing:border-box;margin:0;padding:0}
  html,body{width:963px;height:1200px;overflow:hidden;background:var(--stage)}
  body{position:relative;font-family:"Poppins",sans-serif}
  .flyer{
    position:absolute;left:124px;top:94px;width:716px;height:1012px;
    background:var(--white);overflow:hidden;
    box-shadow:6px 8px 14px rgba(0,0,0,.35);
  }
  .hero-art{position:absolute;left:0;top:0;width:716px;height:476px}
  .abs{position:absolute}
  .based{right:32px;top:40px;text-align:right;color:var(--white)}
  .based h2{font-family:"Roboto Condensed",sans-serif;font-weight:700;color:var(--red);font-size:27px;line-height:1;letter-spacing:.2px}
  .based p{font-size:11px;line-height:1.3;margin-top:3px;letter-spacing:.2px}
  .brand{left:47px;top:96px;font-family:"Poppins",sans-serif;font-weight:600;font-size:44px;color:var(--red);letter-spacing:-.5px;line-height:1}
  .headline{left:47px;top:196px}
  .headline .kicker{font-weight:600;font-size:21px;color:var(--ink);line-height:1}
  .headline .big{font-family:"Roboto Condensed",sans-serif;font-weight:700;font-size:66px;line-height:.96;letter-spacing:-1px}
  .headline .red{color:var(--red);margin-top:6px}
  .headline .ink{color:var(--ink)}
  .rule{left:47px;top:360px;width:96px;height:3px;background:var(--red)}
  .intro{left:47px;top:375px;font-size:17px;line-height:21px;color:var(--ink)}

  .services{position:absolute;left:0;top:476px;width:716px;height:189px;background:var(--dark)}
  .service{position:absolute;top:-9px;width:200px;margin-left:-100px;text-align:center;color:var(--white)}
  .service .badge{display:block;margin:0 auto;width:76px;height:76px}
  .service h3{font-weight:600;font-size:16px;line-height:21px;margin-top:4px;letter-spacing:.2px}
  .service .dash{width:38px;height:2px;background:var(--red);margin:5px auto 8px}
  .service p{font-size:12px;line-height:13.5px}

  .values{position:absolute;left:0;top:665px;width:716px;height:148px;background:var(--white)}
  .family-icon{position:absolute;left:45px;top:48px;width:64px;height:64px}
  .family{position:absolute;left:122px;top:24px;font-family:"Roboto Condensed",sans-serif;font-weight:700;font-size:33px;line-height:34px;color:var(--ink)}
  .family .red{color:var(--red)}
  .divider{position:absolute;left:343px;top:26px;width:1px;height:96px;background:var(--ink)}
  .points{position:absolute;left:376px;top:28px;list-style:none}
  .points li{display:flex;align-items:center;height:26.5px;font-weight:500;font-size:16px;color:var(--ink)}
  .points svg{width:13px;height:13px;margin-right:9px;flex:none}

  .contact{position:absolute;left:0;top:813px;width:716px;height:128px;background:var(--dark)}
  .touch{position:absolute;left:47px;top:38px}
  .touch h2{font-family:"Roboto Condensed",sans-serif;font-weight:700;font-size:34px;line-height:1;color:var(--red)}
  .touch p{font-size:8.6px;color:var(--white);margin-top:6px;font-weight:500}
  .person{position:absolute;top:42px}
  .person .name{display:flex;align-items:center;font-family:"Roboto Condensed",sans-serif;font-weight:700;font-size:22px;line-height:1;color:var(--red)}
  .person .name svg{width:13px;height:13px;margin-right:3px}
  .person .phone{font-family:"Roboto Condensed",sans-serif;font-size:22px;color:var(--white);margin-top:6px;line-height:1}

  .email-bar{position:absolute;left:0;top:941px;width:716px;height:71px;background:var(--red)}
  .slashes{position:absolute;top:27px;width:84px;height:18px}
  .email{position:absolute;left:0;right:0;top:0;height:71px;display:flex;align-items:center;justify-content:center;
    font-family:"Roboto Condensed",sans-serif;font-weight:600;font-size:22px;letter-spacing:1.2px;color:var(--white)}
  .email svg{width:22px;height:22px;margin-right:5px}
</style>
</head>
<body>
<main class="flyer">

  <svg class="hero-art" viewBox="0 0 716 476" aria-hidden="false">
    <defs>
      <linearGradient id="yard" x1="0" y1="0" x2="0" y2="1">
        <stop offset="0" stop-color="var(--sky-top)"/>
        <stop offset=".28" stop-color="var(--sky-low)"/>
        <stop offset=".45" stop-color="#b8bcc2"/>
        <stop offset=".62" stop-color="#e8e8e6"/>
        <stop offset=".7" stop-color="#9a9da2"/>
        <stop offset="1" stop-color="var(--concrete)"/>
      </linearGradient>
    </defs>
    <polygon points="405,0 716,0 716,105 380,105" fill="var(--dark)"/>
    <polygon points="382,0 407,0 382,105 357,105" fill="var(--red)"/>
    <polygon points="348,105 362,105 290,476 258,476" fill="var(--light-grey)"/>
    <polygon points="358,105 716,105 716,476 284,476" fill="url(#yard)" role="img"
      aria-label="Photo: white fuel tanker trucks parked in front of a depot shed under a blue cloudy sky"/>
  </svg>

  <div class="abs based">
    <h2>BASED IN GRIFFITH NSW</h2>
    <p>SERVICING GRIFFITH AREA AND SURROUNDS</p>
  </div>

  <div class="abs brand">Terra Diesel</div>

  <div class="abs headline">
    <div class="kicker">YOUR LOCAL</div>
    <div class="big red">BULK FUEL</div>
    <div class="big ink">SUPPLIER</div>
  </div>
  <div class="abs rule"></div>
  <p class="abs intro">Bulk petroleum supplier,<br>servicing any industry<br>that requires diesel.</p>

  <section class="services">
    <div class="service" style="left:146px">
      <svg class="badge" viewBox="0 0 76 76">
        <circle cx="38" cy="38" r="36" fill="var(--red)" stroke="#fff" stroke-width="2.5"/>
        <g fill="none" stroke="#fff" stroke-width="2.2" stroke-linejoin="round">
          <rect x="17" y="27" width="25" height="16" rx="2"/>
          <path d="M42 31h9l7 7v5H42z"/>
          <circle cx="24" cy="46" r="3"/><circle cx="50" cy="46" r="3"/>
          <path d="M29 31c-2 3-3 4-3 6a3 3 0 0 0 6 0c0-2-1-3-3-6z"/>
        </g>
      </svg>
      <h3>BULK FUEL<br>DELIVERIES</h3>
      <div class="dash"></div>
      <p>Reliable bulk diesel<br>deliveries when and<br>where you need it.</p>
    </div>
    <div class="service" style="left:350px">
      <svg class="badge" viewBox="0 0 76 76">
        <circle cx="38" cy="38" r="36" fill="var(--red)" stroke="#fff" stroke-width="2.5"/>
        <g fill="none" stroke="#fff" stroke-width="2.2" stroke-linejoin="round" stroke-linecap="round">
          <path d="M20 33h6l4 3h14l12-5-9 13H30l-4-6h-6z"/>
          <path d="M34 36v-4h6v4M33 32h8"/>
          <path d="M59 40c-1 2-2 3-2 4a2 2 0 0 0 4 0c0-1-1-2-2-4z"/>
        </g>
      </svg>
      <h3>OILS &amp;<br>LUBRICANTS</h3>
      <div class="dash"></div>
      <p>Quality oils and<br>lubricants to keep your<br>equipment running</p>
    </div>
    <div class="service" style="left:553px">
      <svg class="badge" viewBox="0 0 76 76">
        <circle cx="38" cy="38" r="36" fill="var(--red)" stroke="#fff" stroke-width="2.5"/>
        <g fill="none" stroke="#fff" stroke-width="2.2" stroke-linejoin="round" stroke-linecap="round">
          <path d="M27 24h20a3 3 0 0 1 3 3v24a3 3 0 0 1-3 3H29a3 3 0 0 1-3-3V31z"/>
          <path d="M31 20h8M33 24v-4"/>
          <path d="M38 33c-4 5-5 8-5 10a5 5 0 0 0 10 0c0-2-1-5-5-10z"/>
        </g>
      </svg>
      <h3>PETROL<br>DELIVERIES</h3>
      <div class="dash"></div>
      <p>Petrol deliveries<br>for equipment,<br>vehicles and more.</p>
    </div>
  </section>

  <section class="values">
    <svg class="family-icon" viewBox="0 0 64 64">
      <circle cx="32" cy="32" r="30" fill="none" stroke="var(--ink)" stroke-width="2"/>
      <g fill="none" stroke="var(--red)" stroke-width="2" stroke-linejoin="round">
        <path d="M14 32l18-15 18 15M18 29v18"/>
        <rect x="22" y="40" width="5" height="7"/>
        <rect x="30" y="34" width="5" height="13"/>
        <rect x="38" y="28" width="5" height="19"/>
      </g>
    </svg>
    <div class="family">LOCAL<br><span class="red">FAMILY OWNED</span><br>BUSINESS</div>
    <div class="divider"></div>
    <ul class="points">
      <li><svg viewBox="0 0 13 13"><circle cx="6.5" cy="6.5" r="6.5" fill="var(--red)"/><path d="M3.6 6.7l2 2 3.8-4" fill="none" stroke="#fff" stroke-width="1.5"/></svg>LOCAL PEOPLE, LOCAL SERVICE</li>
      <li><svg viewBox="0 0 13 13"><circle cx="6.5" cy="6.5" r="6.5" fill="var(--red)"/><path d="M3.6 6.7l2 2 3.8-4" fill="none" stroke="#fff" stroke-width="1.5"/></svg>RELIABLE &amp; ON TIME</li>
      <li><svg viewBox="0 0 13 13"><circle cx="6.5" cy="6.5" r="6.5" fill="var(--red)"/><path d="M3.6 6.7l2 2 3.8-4" fill="none" stroke="#fff" stroke-width="1.5"/></svg>COMPETITIVE PRICING</li>
      <li><svg viewBox="0 0 13 13"><circle cx="6.5" cy="6.5" r="6.5" fill="var(--red)"/><path d="M3.6 6.7l2 2 3.8-4" fill="none" stroke="#fff" stroke-width="1.5"/></svg>SUPPORTING LOCAL INDUSTRY</li>
    </ul>
  </section>

  <section class="contact">
    <div class="touch">
      <h2>GET IN TOUCH</h2>
      <p>WE'RE LOCAL, RELIABLE AND READY TO HELP.</p>
    </div>
    <div class="person" style="left:288px">
      <div class="name"><svg viewBox="0 0 13 13"><circle cx="6.5" cy="6.5" r="6.5" fill="var(--red)"/><path d="M4 3.5l1.5 1.5-1 1c.6 1.2 1.4 2 2.5 2.5l1-1L9.5 9 8.5 10C6 9.6 3.4 7 3 4.5z" fill="#fff"/></svg>MARCO</div>
      <div class="phone">0412 309 768</div>
    </div>
    <div class="person" style="left:425px">
      <div class="name"><svg viewBox="0 0 13 13"><circle cx="6.5" cy="6.5" r="6.5" fill="var(--red)"/><path d="M4 3.5l1.5 1.5-1 1c.6 1.2 1.4 2 2.5 2.5l1-1L9.5 9 8.5 10C6 9.6 3.4 7 3 4.5z" fill="#fff"/></svg>LIAM</div>
      <div class="phone">0431 672 095</div>
    </div>
    <div class="person" style="left:559px">
      <div class="name"><svg viewBox="0 0 13 13"><circle cx="6.5" cy="6.5" r="6.5" fill="var(--red)"/><path d="M4 3.5l1.5 1.5-1 1c.6 1.2 1.4 2 2.5 2.5l1-1L9.5 9 8.5 10C6 9.6 3.4 7 3 4.5z" fill="#fff"/></svg>SIMON</div>
      <div class="phone">0465 218 347</div>
    </div>
  </section>

  <section class="email-bar">
    <svg class="slashes" style="left:53px" viewBox="0 0 84 18"><g stroke="#fff" stroke-opacity=".55" stroke-width="3"><path d="M6 17l6-16M20 17l6-16M34 17l6-16M48 17l6-16M62 17l6-16M76 17l6-16"/></g></svg>
    <div class="email">
      <svg viewBox="0 0 22 22"><circle cx="11" cy="11" r="10" fill="#fff"/><path d="M6 6c2 0 3 2 2 4s1 3 0 5M13 4c0 2 2 2 3 4s-1 3 1 5M12 15c1 0 2 1 2 3" fill="none" stroke="var(--red)" stroke-width="1.6"/></svg>
      Fuel@terradiesel-example.com.au
    </div>
    <svg class="slashes" style="left:581px" viewBox="0 0 84 18"><g stroke="#fff" stroke-opacity=".55" stroke-width="3"><path d="M6 17l6-16M20 17l6-16M34 17l6-16M48 17l6-16M62 17l6-16M76 17l6-16"/></g></svg>
  </section>

</main>
</body>
</html>
```